Solar Advertising Flier to generate Biz

I need a advertisement that generates business to be used in a mailer for marketing purposes.

Im attaching a file that is a an idea of advertisement.
I do not want the "ZVN" specific information on it.
I want the background solar panels.
Same information as the ad.
And I've attached my Logo - I want the color scheme to match this.

Thank you

Target Market(s)

Middle to Upper Class Home Owners

Industry/Entity Type

Solar Energy

Requirements
Must have
• A call to action
• A professional look
Nice to have
• A family
• Great looking solar panels
Should not have
• Cartoons

```html
<!DOCTYPE html>
<html lang="en">
<head>
<meta charset="utf-8">
<title>Go Solar – Bright Acre Energy</title>
<link rel="stylesheet" href="https://fonts.googleapis.com/css2?family=Montserrat:wght@800&family=Open+Sans:wght@400;600;700;800&display=swap">
<style>
  :root {
    --navy: #1d3a7a;
    --navy-deep: #16306a;
    --panel-blue: #2c63b4;
    --sky: #1a8fd0;
    --green: #8cc63f;
    --green-deep: #5fa52d;
    --yellow: #f7d117;
    --orange: #f39a1e;
    --orange-light: #fcd34a;
    --rebate-red: #e8531d;
    --ink: #1f2a52;
    --body-grey: #3a3f4a;
    --white: #ffffff;
  }
  * { box-sizing: border-box; margin: 0; padding: 0; }
  html, body { width: 898px; height: 1200px; overflow: hidden; background: #e9e9e9; }
  .flier {
    position: relative; width: 898px; height: 1200px; overflow: hidden;
    background: var(--white);
    font-family: "Open Sans", Arial, sans-serif;
  }
  .solar-panels {
    position: absolute; left: 0; top: 0; width: 898px; height: 540px;
    background:
      linear-gradient(180deg, var(--navy-deep) 0%, var(--navy) 22%, var(--panel-blue) 48%, #4d86cf 70%, #9cc3ea 100%);
  }
  .panel-curve { position: absolute; left: 0; top: 0; }
  .headline {
    position: absolute; top: 42px; width: 100%; text-align: center;
    font-family: "Montserrat", Arial, sans-serif; font-weight: 800;
    font-size: 140px; letter-spacing: -3px; line-height: 1;
    text-shadow: 0 4px 8px rgba(0,0,0,.35);
  }
  .headline .go { color: var(--white); }
  .headline .solar { color: var(--green); }
  .tagline {
    position: absolute; top: 188px; width: 100%; text-align: center;
    color: var(--yellow); font-weight: 700; font-size: 27px; letter-spacing: -.3px;
  }
  .brand-disc {
    position: absolute; left: 336px; top: 304px; width: 230px; height: 230px;
    border-radius: 50%; background: var(--white);
    box-shadow: 0 0 0 6px rgba(255,255,255,.6);
  }
  .house-photo {
    position: absolute; left: 0; top: 600px; width: 898px; height: 470px;
    background: linear-gradient(180deg, rgba(255,255,255,0) 0%, rgba(214,170,150,.35) 25%, rgba(190,200,215,.45) 55%, rgba(170,200,150,.45) 100%);
  }
  .brand-name {
    position: absolute; top: 548px; width: 100%; text-align: center;
    color: var(--sky); font-weight: 600; line-height: 1.05;
  }
  .brand-name .main { display: block; font-size: 54px; }
  .brand-name .sub { display: block; font-size: 30px; letter-spacing: 4px; }
  .promise {
    position: absolute; left: 158px; top: 654px; width: 582px; height: 58px;
    border-radius: 29px;
    background: linear-gradient(180deg, var(--orange-light), var(--orange));
    box-shadow: 0 3px 6px rgba(0,0,0,.25);
    color: var(--white); font-weight: 700; font-size: 44px; line-height: 58px; text-align: center;
  }
  .benefits { position: absolute; left: 28px; top: 760px; width: 440px; list-style: none; }
  .benefits li {
    position: relative; padding-left: 38px; margin-bottom: 16px;
    color: var(--ink); font-weight: 600; font-size: 21px; line-height: 1.3;
  }
  .benefits svg { position: absolute; left: 0; top: 4px; }
  .how-it-works { position: absolute; left: 490px; top: 758px; width: 386px; }
  .how-it-works h2 { color: var(--ink); font-weight: 700; font-size: 26px; margin-bottom: 8px; }
  .how-it-works h2 span { margin-right: 18px; }
  .how-it-works p {
    color: var(--body-grey); font-size: 18.5px; line-height: 1.45; text-align: left;
  }
  .footer-shapes { position: absolute; left: 0; top: 0; }
  .consult {
    position: absolute; left: 43px; top: 1088px; color: var(--white);
    font-weight: 600; font-size: 19.5px; line-height: 1.35;
  }
  .phone {
    position: absolute; left: 40px; top: 1140px; color: var(--white);
    font-weight: 600; font-size: 36px; display: flex; align-items: center; gap: 12px;
  }
  .rebate {
    position: absolute; left: 555px; top: 986px; width: 340px; text-align: center;
    color: var(--ink); font-weight: 800;
  }
  .rebate .lead { font-size: 28px; line-height: 1.2; }
  .rebate .amount {
    font-family: "Montserrat", Arial, sans-serif; font-weight: 800;
    color: var(--rebate-red); font-size: 104px; line-height: 1.02; letter-spacing: -3px;
    text-shadow: 0 3px 4px rgba(0,0,0,.25);
  }
  .rebate .tail { font-size: 28px; line-height: 1.1; }
</style>
</head>
<body>
<main class="flier">
  <div class="solar-panels" role="img" aria-label="Close-up of rows of blue solar panels under the sky"></div>

  <svg class="panel-curve" width="898" height="600" viewBox="0 0 898 600" aria-hidden="true">
    <path d="M0 440 Q449 572 898 440 L898 600 L0 600 Z" fill="var(--green)"/>
    <path d="M0 466 Q449 588 898 466 L898 600 L0 600 Z" fill="var(--white)"/>
  </svg>

  <div class="house-photo" role="img" aria-label="Faded photo of a tiled house roof fitted with solar panels"></div>

  <h1 class="headline"><span class="go">GO</span> <span class="solar">SOLAR</span></h1>
  <p class="tagline">GET GRANDFATHERED BEFORE THE NEW UTILITY DEADLINE</p>

  <div class="brand-disc" aria-hidden="true"></div>
  <p class="brand-name"><span class="main">BRIGHT ACRE</span><span class="sub">ENERGY</span></p>

  <p class="promise">WE MAKE IT EASE</p>

  <ul class="benefits">
    <li><svg width="26" height="26" viewBox="0 0 26 26"><circle cx="13" cy="13" r="11" fill="none" stroke="var(--ink)" stroke-width="2"/><path d="M7.5 13 L11.5 17 L19 9" fill="none" stroke="var(--sky)" stroke-width="2.6" stroke-linecap="round"/></svg>$0 Down, no upfront cost</li>
    <li><svg width="26" height="26" viewBox="0 0 26 26"><circle cx="13" cy="13" r="11" fill="none" stroke="var(--ink)" stroke-width="2"/><path d="M7.5 13 L11.5 17 L19 9" fill="none" stroke="var(--sky)" stroke-width="2.6" stroke-linecap="round"/></svg>Save up to 90% off your utillity bill</li>
    <li><svg width="26" height="26" viewBox="0 0 26 26"><circle cx="13" cy="13" r="11" fill="none" stroke="var(--ink)" stroke-width="2"/><path d="M7.5 13 L11.5 17 L19 9" fill="none" stroke="var(--sky)" stroke-width="2.6" stroke-linecap="round"/></svg>Protect against inflation and energy costs increases from your Utillity Company</li>
    <li><svg width="26" height="26" viewBox="0 0 26 26"><circle cx="13" cy="13" r="11" fill="none" stroke="var(--ink)" stroke-width="2"/><path d="M7.5 13 L11.5 17 L19 9" fill="none" stroke="var(--sky)" stroke-width="2.6" stroke-linecap="round"/></svg>Provide clean, reliable energy for your family power by the sun</li>
  </ul>

  <section class="how-it-works">
    <h2><span>&#10095;&#10095;</span>HOW IT WORKS</h2>
    <p>Your solar system allows you to generate your own clean power and COST LESS than your current utillity company. Simply pay by the month, like you do now... but at a LOWER rate and START SAVING IMMEDIATELY!!!</p>
  </section>

  <svg class="footer-shapes" width="898" height="1200" viewBox="0 0 898 1200" aria-hidden="true">
    <defs>
      <linearGradient id="footerGreen" x1="0" y1="0" x2="1" y2="0">
        <stop offset="0" stop-color="var(--green-deep)"/>
        <stop offset="1" stop-color="var(--green)"/>
      </linearGradient>
      <radialGradient id="rebateGlow" cx=".4" cy=".35" r=".75">
        <stop offset="0" stop-color="#fde21a"/>
        <stop offset=".6" stop-color="#fbc51c"/>
        <stop offset="1" stop-color="var(--orange)"/>
      </radialGradient>
    </defs>
    <path d="M0 1060 Q300 1008 620 1010 L620 1200 L0 1200 Z" fill="var(--white)"/>
    <path d="M0 1074 Q300 1024 620 1024 L620 1200 L0 1200 Z" fill="url(#footerGreen)"/>
    <path d="M495 1200 Q490 1010 640 975 Q780 950 898 985 L898 1200 Z" fill="url(#rebateGlow)"/>
  </svg>

  <p class="consult">CALL TODAY FOR A NO<br>OBLIGATION CONSULTATION</p>
  <p class="phone">
    <svg width="36" height="36" viewBox="0 0 36 36" aria-hidden="true"><circle cx="18" cy="18" r="15.5" fill="none" stroke="var(--white)" stroke-width="2.5"/><path d="M12.5 10.5 l3 -1 l2 5 l-2 1.5 q1.5 3.5 5 5 l1.5 -2 l5 2 l-1 3 q-1 1.5 -3 1.5 q-6.5 -1 -11 -6.5 q-1.5 -2.5 -1.5 -5 q0 -2 2 -3.5 Z" fill="var(--white)"/></svg>
    0000000000
  </p>

  <div class="rebate">
    <p class="lead">CALL TODAY<br>AND RECEIVE A</p>
    <p class="amount">$500</p>
    <p class="tail">CASH REBATE</p>
  </div>
</main>
</body>
</html>
```